Surviving Domestic Violence Flyer

I need a flyer that "POPS" to attract participants for my research project. I have added the important information on my draft flyer.

```html
<!DOCTYPE html>
<html lang="en">
<head>
<meta charset="utf-8">
<title>Perceived Effectiveness of Domestic Violence Services – Study Flyer</title>
<link href="https://fonts.googleapis.com/css2?family=Open+Sans:wght@400;600;700&family=Tenor+Sans&display=swap" rel="stylesheet">
<style>
  :root {
    --page: #ffffff;
    --flyer: #000000;
    --white: #f1f1f1;
    --soft-grey: #b9b9b9;
    --body-grey: #7a7a7a;
    --blush: #efb6a6;
    --tab: #e6ada1;
    --tab-ink: #1a1a1a;
  }
  * { margin: 0; padding: 0; box-sizing: border-box; }
  html, body {
    width: 1200px; height: 1200px; overflow: hidden;
    background: var(--page);
  }
  .flyer {
    position: absolute; left: 160px; top: 32px;
    width: 880px; height: 1136px;
    background: var(--flyer);
    font-family: "Open Sans", Arial, sans-serif;
    color: var(--white);
    overflow: hidden;
  }
  .hero-photo {
    position: absolute; left: 0; top: 0; width: 880px; height: 440px;
    background:
      radial-gradient(ellipse 300px 260px at 430px 170px, #8a7064 0%, #4a3a34 45%, rgba(0,0,0,0) 100%),
      linear-gradient(90deg, #3c3c3c 0%, #2a2a2a 30%, #1a1512 60%, #000 85%),
      #000;
  }
  .hero-photo::after {
    content: ""; position: absolute; inset: 0;
    background: linear-gradient(180deg, rgba(0,0,0,0) 60%, #000 100%);
  }
  .call-out {
    position: absolute; right: 71px; top: 58px;
    text-align: right;
  }
  .call-out .request {
    font-size: 20px; line-height: 28px; color: var(--soft-grey);
  }
  .call-out .study-title {
    font-size: 23px; line-height: 31px; font-weight: 600;
    text-transform: uppercase; color: var(--white);
  }
  .headline {
    position: absolute; left: 0; width: 880px; top: 373px;
    text-align: center;
    font-family: "Tenor Sans", "Optima", sans-serif;
    font-size: 39px; line-height: 54px; letter-spacing: 3px;
    font-weight: 700; color: var(--white);
    text-transform: uppercase;
  }
  .screening {
    position: absolute; left: 0; width: 880px; top: 505px;
    list-style: none; text-align: center;
    font-size: 21px; line-height: 32.2px; letter-spacing: 0.3px;
    color: var(--blush); text-transform: uppercase;
  }
  .details {
    position: absolute; left: 20px; width: 840px; top: 730px;
    text-align: center; font-size: 15.5px; line-height: 20px;
    color: var(--body-grey);
  }
  .details p + p { margin-top: 22px; }
  .credits {
    position: absolute; left: 0; width: 880px; top: 853px;
    text-align: center; font-size: 15.5px; line-height: 20.4px;
    color: var(--body-grey);
  }
  .credits b { font-weight: 700; }
  .tear-tabs {
    position: absolute; left: 8px; top: 934px;
    display: flex; gap: 10.5px;
  }
  .tab {
    width: 57px; height: 196px; background: var(--tab);
    display: flex; align-items: flex-end; justify-content: center;
    padding-bottom: 8px;
  }
  .tab span {
    writing-mode: vertical-rl; transform: rotate(180deg);
    font-size: 14.5px; line-height: 19px; color: var(--tab-ink);
    white-space: nowrap;
  }
</style>
</head>
<body>
  <main class="flyer">
    <div class="hero-photo" role="img" aria-label="Dramatic dark photograph of a frightened woman peering out through window blinds"></div>

    <div class="call-out">
      <p class="request">Request for<br>Study Participants</p>
      <p class="study-title">Efficiency of<br>Resources<br>Available to<br>Suvivors of<br>Intimate<br>Partner<br>Abuse</p>
    </div>

    <h1 class="headline">Perceived Effectiveness of<br>Domestic Violence Services</h1>

    <ul class="screening">
      <li>"Are you eighteen years of age or older?"</li>
      <li>"Have you been a victim of domestic violence?"</li>
      <li>"Have you sought assistance with abuse in the last 12 months?"</li>
      <li>"Are you still in contact with the person who abused you?"</li>
      <li>"Are you willing and open to discussing your experience with<br>abuse and your attempts to access services or resources?"</li>
    </ul>

    <div class="details">
      <p>If you answered yes to all of these questions, you may be eligible t participate in a study to better<br>understand the resources needed and services expected for survivors of domestic violence.</p>
      <p>Plese contact Dana Whitfield at 1(555)014-2290 or via e-mail survivorstudy@example.org<br>for additional information. Participants will be compensated for their time.</p>
    </div>

    <div class="credits">
      <p><b>Principal Investigator:</b> Dana Whitfield</p>
      <p><b>Institutional Addiliation:</b> Lakeshore State University, Dept. of Criminology,Law, and Justice</p>
      <p><b>Contact Address:</b> Post Office Box 10452, Riverton, IL 60000</p>
    </div>

    <div class="tear-tabs">
      <div class="tab"><span>Survivor Resources Study<br>1(555)014-2290</span></div>
      <div class="tab"><span>Survivor Resources Study<br>1(555)014-2290</span></div>
      <div class="tab"><span>Survivor Resources Study<br>1(555)014-2290</span></div>
      <div class="tab"><span>Survivor Resources Study<br>1(555)014-2290</span></div>
      <div class="tab"><span>Survivor Resources Study<br>1(555)014-2290</span></div>
      <div class="tab"><span>Survivor Resources Study<br>1(555)014-2290</span></div>
      <div class="tab"><span>Survivor Resources Study<br>1(555)014-2290</span></div>
      <div class="tab"><span>Survivor Resources Study<br>1(555)014-2290</span></div>
      <div class="tab"><span>Survivor Resources Study<br>1(555)014-2290</span></div>
      <div class="tab"><span>Survivor Resources Study<br>1(555)014-2290</span></div>
      <div class="tab"><span>Survivor Resources Study<br>1(555)014-2290</span></div>
      <div class="tab"><span>Survivor Resources Study<br>1(555)014-2290</span></div>
      <div class="tab"><span>Survivor Resources Study<br>1(555)014-2290</span></div>
    </div>
  </main>
</body>
</html>
```